Harbor of Kitchencraft Podcast Episode Cover

I’m looking for a clean, professional, and eye-catching podcast episode cover template for my show, Harbor of Kitchencraft. Each week, I feature a new guest, so the design must allow me (or my team) to easily swap in a new guest’s photo without needing advanced design skills.

The template should be:

- Drag-and-drop friendly: simple for me to replace the guest’s headshot in Canva, Photoshop, or similar.
- On-brand with the Harbor of Kitchencraft podcast: professional yet approachable, foodservice industry-focused.
- Bold and attention-grabbing for podcast platforms and social media.

Readable text at small sizes, since covers are often viewed as thumbnails.

Design Elements to Include:

1. Podcast Title: “Harbor of Kitchencraft” (prominently displayed)
2. Subtitle/Space: Line for guest’s name, professional title, and company name
3. Photo Placeholder: Large, central area where I can easily drag and drop a guest photo
4. Brand Colors: attached
5. Clean, modern fonts (easy to read at thumbnail size)
6. Background graphics or patterns that give a sense of foodservice, leadership, or nationwide reach... but do not overpower the guest photo

Format Requirements:

- Editable source file (PSD, Canva template, or layered AI/INDD)
- JPG/PNG exports for immediate use
- Square format (3000x3000px) for podcast platforms

Style Inspiration:
Think modern podcast covers: bold fonts, clean lines, professional with a touch of energy.

Deliverables:

1. Final episode cover template (editable file)
2. Instructions or guidance on how to swap out guest photos

```html
<!DOCTYPE html>
<html lang="en">
<head>
<meta charset="utf-8">
<title>Harbor of Kitchencraft Podcast — Episode Cover</title>
<link rel="stylesheet" href="https://fonts.googleapis.com/css2?family=Bebas+Neue&family=Poppins:wght@400;500;800&display=swap">
<style>
  :root {
    --brand-yellow: #f7b516;
    --ink-white: #ffffff;
    --night-blue: #12273d;
    --steel-blue: #2f5d82;
    --warm-glow: #8a7440;
    --band-dark: #0f1c2a;
    --portrait-sky: #c9d3dc;
    --portrait-suit: #2c3d55;
  }
  * { box-sizing: border-box; margin: 0; padding: 0; }
  html, body { width: 1200px; height: 1200px; overflow: hidden; background: #e2e2e2; }
  .cover {
    position: relative;
    width: 1200px;
    height: 1200px;
    overflow: hidden;
    font-family: "Poppins", sans-serif;
    color: var(--ink-white);
  }
  .kitchen-backdrop {
    position: absolute; inset: 0;
    background:
      radial-gradient(ellipse 45% 30% at 55% 52%, rgba(190,160,80,.55), transparent 70%),
      radial-gradient(ellipse 30% 25% at 85% 75%, rgba(110,140,90,.45), transparent 70%),
      linear-gradient(180deg, var(--steel-blue) 0%, #2a506f 40%, #3d5a62 60%, var(--night-blue) 100%);
  }
  .bottom-shade {
    position: absolute; left: 0; right: 0; bottom: 0; height: 520px;
    background: linear-gradient(180deg, transparent 0%, rgba(10,20,32,.55) 55%, rgba(10,20,32,.8) 100%);
  }
  .show-title {
    position: absolute; left: 0; right: 0; top: 60px;
    text-align: center;
    font-family: "Bebas Neue", sans-serif;
    line-height: 1;
    text-shadow: 0 4px 12px rgba(0,0,0,.35);
  }
  .show-title__top { display: block; font-size: 222px; color: var(--ink-white); height: 178px; }
  .show-title__main { display: block; font-size: 178px; color: var(--brand-yellow); height: 150px; margin-top: 6px; }
  .show-label {
    position: absolute; left: 0; right: 0; top: 386px;
    text-align: center;
    font-size: 36px; font-weight: 500; letter-spacing: 16px;
    padding-left: 16px;
  }
  .divider-band {
    position: absolute; left: 0; right: 0; top: 676px; height: 34px;
    background: var(--brand-yellow);
  }
  .portrait-ring {
    position: absolute; left: 350px; top: 443px; width: 500px; height: 500px;
    border-radius: 50%;
    background: var(--brand-yellow);
    box-shadow: 0 8px 28px rgba(0,0,0,.35);
  }
  .portrait-frame {
    position: absolute; left: 32px; top: 32px; width: 436px; height: 436px;
    border-radius: 50%; background: var(--ink-white);
  }
  .guest-photo {
    position: absolute; left: 12px; top: 12px; width: 412px; height: 412px;
    border-radius: 50%;
    background:
      radial-gradient(ellipse 55% 35% at 50% 100%, var(--portrait-suit) 60%, transparent 62%),
      linear-gradient(180deg, var(--portrait-sky) 0%, #9fb0bf 55%, #5f7488 100%);
  }
  .guest-label {
    position: absolute; left: 0; right: 0; top: 968px;
    text-align: center; font-size: 26px; font-weight: 500; letter-spacing: 10px; padding-left: 10px;
  }
  .guest-name {
    position: absolute; left: 0; right: 0; top: 990px;
    text-align: center; font-size: 90px; font-weight: 800; line-height: 1.05;
    color: var(--brand-yellow); letter-spacing: 4px;
  }
  .guest-role {
    position: absolute; left: 0; right: 0; top: 1077px;
    text-align: center; font-size: 21px; font-weight: 400; letter-spacing: 6px; padding-left: 6px;
  }
  .company-band {
    position: absolute; left: 0; right: 0; top: 1103px; height: 64px;
    background: linear-gradient(90deg, var(--band-dark) 15%, rgba(247,181,22,.9) 50%, var(--band-dark) 85%);
    opacity: .95;
  }
  .company-name {
    position: absolute; left: 0; right: 0; top: 1109px;
    text-align: center; font-size: 34px; font-weight: 500; letter-spacing: 11px; padding-left: 11px;
    text-shadow: 0 2px 6px rgba(0,0,0,.4);
  }
</style>
</head>
<body>
  <main class="cover">
    <div class="kitchen-backdrop" role="img" aria-label="Blurred photo of a busy restaurant kitchen with a chef plating food and a bowl of fresh salad"></div>
    <div class="bottom-shade"></div>

    <h1 class="show-title">
      <span class="show-title__top">HARBOR OF</span>
      <span class="show-title__main">KITCHENCRAFT</span>
    </h1>
    <p class="show-label">PODCAST</p>

    <div class="divider-band"></div>
    <div class="portrait-ring">
      <div class="portrait-frame">
        <div class="guest-photo" role="img" aria-label="Guest headshot: smiling man in a navy blazer and white shirt in front of a building"></div>
      </div>
    </div>

    <p class="guest-label">GUEST</p>
    <h2 class="guest-name">MARA QUILLEN</h2>
    <p class="guest-role">PROFESSIONAL TITLE</p>
    <div class="company-band"></div>
    <p class="company-name">COMPANY NAME</p>
  </main>
</body>
</html>
```